New business card design for Maplewood Ridge Optometry Clinic

We need a new business card design using our existing logo (uploaded). Please do not include eyes, eye exam charts or beaches, water, sand. The logo I uploaded shows our colors of green and blue, but we are open to seeing it in black OR white. We would like to see something modern and fresh. It will need to be 2 sided. On the front we will need to be able to put a doctors name, for example-Dr Clara Venhuisen and Associates. We will need to be able to change the name to other doctors names when we send for printing. The back of the card should list the following: 1748 Tarrow St, Wasaga Beach (P)705-555-0183 (E) info@mroc-example.ca www.mroc-example.ca. "We are welcoming new patients" and a line for the appointment date and time. I have uploaded the back of a card to give an example

```html
<!DOCTYPE html>
<html lang="en">
<head>
<meta charset="utf-8">
<title>Maplewood Ridge Optometry Clinic – Appointment Card</title>
<link rel="stylesheet" href="https://fonts.googleapis.com/css2?family=Lexend:wght@300;700&display=swap">
<style>
  :root {
    --ink: #1e2121;
    --paper: #ffffff;
    --texture: #eceeec;
  }
  * { margin: 0; padding: 0; box-sizing: border-box; }
  html, body { width: 1200px; height: 706px; overflow: hidden; background: var(--paper); }
  .card {
    position: relative;
    width: 1200px;
    height: 706px;
    background: var(--paper);
    color: var(--ink);
    font-family: "Lexend", sans-serif;
    overflow: hidden;
  }
  .texture-area {
    position: absolute;
    left: -60px;
    top: -20px;
    width: 440px;
    height: 740px;
    background: radial-gradient(ellipse 60% 55% at 40% 48%, var(--texture) 0%, rgba(236,238,236,0.6) 55%, rgba(255,255,255,0) 100%);
  }
  .headline {
    position: absolute;
    left: 86px;
    top: 62px;
    width: 1032px;
    font-weight: 700;
    font-size: 64px;
    line-height: 1;
    letter-spacing: 0.5px;
    white-space: nowrap;
  }
  .contact-list { list-style: none; }
  .contact-item {
    position: absolute;
    right: 166px;
    font-weight: 300;
    font-size: 50px;
    line-height: 1;
    letter-spacing: 1px;
    white-space: nowrap;
    text-align: right;
  }
  .contact-item--address { top: 196px; }
  .contact-item--phone   { top: 291px; }
  .contact-item--email   { top: 374px; }
  .contact-item--web     { top: 455px; }
  .contact-icon { position: absolute; fill: var(--ink); }
  .icon-pin   { left: 1091px; top: 194px; width: 42px; height: 68px; }
  .icon-phone { left: 1092px; top: 290px; width: 42px; height: 58px; }
  .icon-mail  { left: 1092px; top: 391px; width: 42px; height: 30px; }
  .icon-globe { left: 1092px; top: 464px; width: 42px; height: 42px; }
  .appointment-label {
    position: absolute;
    top: 583px;
    font-weight: 300;
    font-size: 50px;
    line-height: 1;
    letter-spacing: 1px;
  }
  .appointment-label--date { left: 93px; }
  .appointment-label--time { left: 621px; }
  .write-line {
    position: absolute;
    top: 632px;
    height: 4px;
    background: var(--ink);
  }
  .write-line--date { left: 245px; width: 305px; }
  .write-line--time { left: 777px; width: 303px; }
</style>
</head>
<body>
<main class="card">
  <div class="texture-area" role="img" aria-label="Soft light grey dotted wave texture"></div>

  <h1 class="headline">We are welcoming new patients!</h1>

  <ul class="contact-list">
    <li class="contact-item contact-item--address">1748 Tarrow St, Wasaga Beach</li>
    <li class="contact-item contact-item--phone">705-555-0183</li>
    <li class="contact-item contact-item--email">info@mroc-example.ca</li>
    <li class="contact-item contact-item--web">www.mroc-example.ca</li>
  </ul>

  <svg class="contact-icon icon-pin" viewBox="0 0 42 68" aria-hidden="true">
    <path fill-rule="evenodd" d="M21 0C9.4 0 0 9 0 20.5 0 34 16 58 19 66c.8 2 3.2 2 4 0 3-8 19-32 19-45.5C42 9 32.6 0 21 0Zm0 12a9 9 0 1 1 0 18 9 9 0 0 1 0-18Zm0 5a4 4 0 1 0 0 8 4 4 0 0 0 0-8Z"/>
  </svg>

  <svg class="contact-icon icon-phone" viewBox="0 0 42 58" aria-hidden="true">
    <path d="M9 0h4c1.3 0 2 .8 2 2v12c0 1.2-.7 2-2 2H11c-1 0-1 1-1 2 .5 10 5 20 12 27 .8.8 1.6.8 2.4.2l1.6-1.3c.9-.7 2-.7 2.8 0l9.5 8c1 .8 1 2 .2 2.8C36 57 32 58.5 28 58 17 56 4 42 2 24 1 15 2 6 5 2c1-1.3 2.4-2 4-2Z"/>
  </svg>

  <svg class="contact-icon icon-mail" viewBox="0 0 42 30" aria-hidden="true">
    <path d="M2 0h38c1.2 0 2 .8 2 2v1L21 16 0 3V2C0 .8.8 0 2 0Zm-2 7 21 13L42 7v21c0 1.2-.8 2-2 2H2c-1.2 0-2-.8-2-2Z"/>
  </svg>

  <svg class="contact-icon icon-globe" viewBox="0 0 42 42" aria-hidden="true">
    <circle cx="21" cy="21" r="20" fill="var(--ink)"/>
    <g fill="none" stroke="#ffffff" stroke-width="2">
      <ellipse cx="21" cy="21" rx="8" ry="20"/>
      <line x1="21" y1="1" x2="21" y2="41"/>
      <line x1="1" y1="21" x2="41" y2="21"/>
      <line x1="4" y1="11" x2="38" y2="11"/>
      <line x1="4" y1="31" x2="38" y2="31"/>
    </g>
  </svg>

  <span class="appointment-label appointment-label--date">Date:</span>
  <span class="write-line write-line--date"></span>
  <span class="appointment-label appointment-label--time">Time:</span>
  <span class="write-line write-line--time"></span>
</main>
</body>
</html>
```